Simple Business Cards for Self-employed Coach

Simple business card with a design that includes the QLT logo.
Using either only the logo color or additional colors that match the logo.

Meridian Guides reach deeply into the past, gathering wisdom from East and West, while still staying current with the frontiers of new discovery in cognitive science, genetics, and other disciplines. see https://www.brightharborpath.example/what-is-integral-coaching/

Target Market(s)

Coaching Clients in Tokyo /Asia; in business organizations, but also outside

Industry/Entity Type

Life Coaching

Contact Information for Business Card

Lukas Brenning
Certified Meridian Guide

3-2-48 Kamiyoshi
Nakarino 164-0392
Tokyo, Japan

Phone: +81 70 4817 5062
E-Mail: lukas.brenning@mailora.example

Font styles to use
Sans Serif

Colors
00a990

Requirements
Must have
• include uploaded logo
• color fitting with QLT logo color
Nice to have
• simple, elegant design
Should not have
• clutter

```html
<!DOCTYPE html>
<html lang="en">
<head>
<meta charset="utf-8">
<title>QLT Business Card – Lukas Brenning</title>
<link rel="stylesheet" href="https://fonts.googleapis.com/css2?family=Open+Sans:wght@400;600;700&display=swap">
<style>
  :root {
    --teal: #00a990;
    --teal-dark: #0e8a78;
    --ink: #3c3c3c;
    --rule: #6a6a6a;
    --slate: #7a7c80;
    --paper: #ffffff;
    --backdrop: #e6e9e9;
  }
  * { margin: 0; padding: 0; box-sizing: border-box; }
  html, body {
    width: 1200px;
    height: 977px;
    overflow: hidden;
    background: var(--backdrop);
    font-family: "Open Sans", Arial, sans-serif;
  }
  .business-card {
    position: absolute;
    left: 150px;
    top: 231px;
    width: 900px;
    height: 514px;
    background: var(--paper);
    box-shadow: 0 6px 24px rgba(0, 0, 0, 0.18);
    overflow: hidden;
    color: var(--ink);
  }
  .brand {
    position: absolute;
    left: 72px;
    top: 82px;
    display: flex;
    align-items: center;
    gap: 18px;
  }
  .brand-square {
    width: 44px;
    height: 44px;
    background: var(--teal-dark);
  }
  .brand-name {
    font-size: 60px;
    font-weight: 600;
    letter-spacing: 10px;
    color: var(--teal-dark);
    line-height: 1;
  }
  .identity {
    position: absolute;
    right: 70px;
    top: 178px;
    text-align: right;
  }
  .person-name {
    font-size: 27px;
    font-weight: 600;
    color: var(--teal-dark);
    line-height: 1.1;
  }
  .person-title {
    font-size: 16px;
    font-weight: 600;
    color: var(--ink);
    margin-top: 3px;
  }
  .divider {
    position: absolute;
    left: 70px;
    right: 70px;
    top: 254px;
    height: 1.5px;
    background: var(--rule);
  }
  .address {
    position: absolute;
    right: 70px;
    top: 266px;
    text-align: right;
    font-size: 17px;
    line-height: 26px;
  }
  .contact-list {
    position: absolute;
    left: 74px;
    top: 266px;
    list-style: none;
    font-size: 17px;
    line-height: 26px;
  }
  .contact-list li {
    display: flex;
    align-items: center;
    gap: 12px;
  }
  .contact-icon {
    width: 16px;
    height: 16px;
    fill: var(--teal);
    flex: none;
  }
  .card-edge {
    position: absolute;
    left: 0;
    bottom: 0;
    width: 900px;
    height: 110px;
  }
  .edge-teal { fill: var(--teal); }
  .edge-slate { fill: var(--slate); }
</style>
</head>
<body>
  <article class="business-card">
    <div class="brand">
      <span class="brand-square"></span>
      <span class="brand-name">QLT</span>
    </div>

    <div class="identity">
      <p class="person-name">Lukas Brenning</p>
      <p class="person-title">Certified Meridian Guide</p>
    </div>

    <div class="divider"></div>

    <address class="address" style="font-style:normal">
      3-2-48 Kamiyoshi<br>
      Nakarino 164-0392, Tokyo, Japan
    </address>

    <ul class="contact-list">
      <li>
        <svg class="contact-icon" viewBox="0 0 24 24" aria-hidden="true"><path d="M6.6 10.8a15.1 15.1 0 0 0 6.6 6.6l2.2-2.2a1 1 0 0 1 1-.25 11.4 11.4 0 0 0 3.6.57 1 1 0 0 1 1 1V20a1 1 0 0 1-1 1A17 17 0 0 1 3 4a1 1 0 0 1 1-1h3.5a1 1 0 0 1 1 1c0 1.25.2 2.45.57 3.57a1 1 0 0 1-.25 1z"/></svg>
        <span>+81 70 4817 5062</span>
      </li>
      <li>
        <svg class="contact-icon" viewBox="0 0 24 24" aria-hidden="true"><path d="M2 5h20v2l-10 6L2 7z"/><path d="M2 9l10 6 10-6v10H2z"/></svg>
        <span>lukas.brenning@mailora.example</span>
      </li>
    </ul>

    <svg class="card-edge" viewBox="0 0 900 110" aria-hidden="true">
      <polygon class="edge-slate" points="838,34 900,34 900,8 856,8"/>
      <polygon class="edge-teal" points="0,110 0,88 812,34 838,34 900,34 900,110"/>
    </svg>
  </article>
</body>
</html>
```